Business Card Design For Financial Company

Create a new design for company's business card. The corporate logo is attached in several formats. Our new website design is also attached and we would like the business cards to reflect this.
Card needs to contain the following info:
Name
Job Title
Legal company name - eg Volmar Capital (Asia) Ltd
Address - eg 612-15 Dorrance Plaza,47 Faverly Street, Hong Kong
Direct tel
Main tel
Fax
Email
Website URL
MS word format preferred. Other formats that can be edited on standard PC also OK.
Please note the the "VOLMAR" logo nameĀ font is "Gill Sans MT" on Windows
Target Market(s)
Instituation Investors
Industry/Entity Type
Business

```html
<!DOCTYPE html>
<html lang="en">
<head>
<meta charset="utf-8">
<title>Volmar Capital – Business Card</title>
<link rel="stylesheet" href="https://fonts.googleapis.com/css2?family=Cabin:wght@400&display=swap">
<style>
  :root {
    --backdrop: #97a2a8;
    --brand-red: #d20f1e;
    --brand-dark: #7a0000;
    --card-white: #ffffff;
    --ink: #2a2a2a;
    --rule: #222222;
  }
  * { margin: 0; padding: 0; box-sizing: border-box; }
  html, body {
    width: 1200px;
    height: 900px;
    overflow: hidden;
  }
  body {
    position: relative;
    background: var(--backdrop);
    font-family: "Cabin", "Gill Sans", sans-serif;
    color: var(--ink);
  }
  .card {
    position: absolute;
    left: 336px;
    width: 607px;
    height: 371px;
    border-radius: 28px;
  }
  .card-front { top: 61px; background: var(--brand-red); }
  .card-back { top: 459px; background: var(--card-white); }

  .brand-mark {
    position: absolute;
    left: 42px;
    top: 198px;
    width: 98px;
    height: 98px;
    border-radius: 50%;
    background: var(--brand-dark);
  }
  .brand-name {
    position: absolute;
    left: 176px;
    top: 216px;
    font-size: 56px;
    line-height: 60px;
    color: var(--card-white);
    letter-spacing: 1px;
  }

  .text-block { position: absolute; font-size: 19px; line-height: 26px; }
  .person { left: 41px; top: 35px; }
  .person-name { color: var(--brand-red); }
  .contact { right: 41px; top: 35px; text-align: right; }
  .web-row {
    position: absolute;
    left: 41px;
    right: 41px;
    top: 171px;
    display: flex;
    align-items: center;
    gap: 8px;
  }
  .web-rule { flex: 1; border-top: 2px dashed var(--rule); }
  .web-url { color: var(--brand-red); font-size: 19px; line-height: 26px; }
  .address { left: 41px; top: 231px; }
  .corner-mark {
    position: absolute;
    left: 510px;
    top: 276px;
    width: 58px;
    height: 58px;
    border-radius: 50%;
    background: var(--brand-dark);
  }
</style>
</head>
<body>
  <section class="card card-front">
    <div class="brand-mark"></div>
    <div class="brand-name">VOLMAR</div>
  </section>

  <section class="card card-back">
    <div class="text-block person">
      <div class="person-name">Daniel Hartley</div>
      <div class="person-title">Sales Manager</div>
    </div>
    <div class="text-block contact">
      <div>main tel: 318 602 4470</div>
      <div>direct tel: 447 219 8305</div>
      <div>fax: 021 596 3148</div>
      <div>contact@volmarcapital.com</div>
    </div>
    <div class="web-row">
      <span class="web-rule"></span>
      <span class="web-url">www.volmarcapital.com</span>
    </div>
    <div class="text-block address">
      <div>Volmar Capital (Asia) Ltd</div>
      <div>612-15 Dorrance Plaza</div>
      <div>47 Faverly Street</div>
      <div>Hong Kong</div>
    </div>
    <div class="corner-mark"></div>
  </section>
</body>
</html>
```